BHP Business Cards

I need business cards for "copper glen partners llc" doublesided... logo on the back (also include logo on front)
logo attached to project... i have jpg up.. let me know if you need eps file.
Company Info:
842 East Marlow Avenue, Suite 7B
Chicago, Illinois 60617
facsimile 312-555-4186 (list fax, address, website on all cards.)
www.copperglenpartnersllc.example
Three different people on cards:
Dorian K. Patel, CPA MST
Principal
ofc 312-555-0271
mobile 312-555-0388
doriankpatel@copperglenpartnersllc.example
Harold J. Quenby, CPA MST
Principal
haroldjquenby@copperglenpartnersllc.example
mobile 708-555-0149
ofc 312-555-0271
Miles T Carver
Principal
ofc 312-555-0271
no mobile
milestcarver@copperglenpartnersllc.example
I have multiple projects listed.. see below:
Business cards for copper glen partners llc
letterhead
envelopes
Business cards for KM Holdings LLC
letterhead
envelopes
rich people
Business

```html
<!DOCTYPE html>
<html lang="en">
<head>
<meta charset="utf-8">
<title>Copper Glen Partners LLC — Stationery</title>
<link rel="stylesheet" href="https://fonts.googleapis.com/css2?family=EB+Garamond:wght@400;700&family=Arimo:wght@400&display=swap">
<style>
  :root{
    --navy:#1b3a6f;
    --navy-deep:#142c57;
    --navy-soft:#5d7bb0;
    --panel:#6b6c6c;
    --paper:#ffffff;
    --ink:#555555;
    --ink-dark:#1d2430;
    --serif:"EB Garamond", Georgia, serif;
    --sans:"Arimo", Arial, sans-serif;
  }
  *{box-sizing:border-box;margin:0;padding:0}
  html,body{width:724px;height:1200px;overflow:hidden;background:#fff}
  .canvas{position:relative;width:724px;height:1200px;background:#fff}
  .stage{position:absolute;left:17px;top:283px;width:690px;height:917px;background:var(--panel)}

  .sheet{position:absolute;background:var(--paper);box-shadow:0 1px 4px rgba(0,0,0,.35);overflow:hidden}
  .band{position:absolute;left:0;display:block}

  .wordmark{position:absolute;font-family:var(--serif);font-weight:400;color:var(--navy);text-transform:uppercase;letter-spacing:.04em;display:flex;align-items:center;gap:6px;white-space:nowrap}
  .wordmark .dot{width:9px;height:9px;border-radius:50%;background:var(--navy);flex:none}

  .contact{position:absolute;font-family:var(--serif);font-weight:700;line-height:1.3;white-space:nowrap}
  .contact.light{color:#fff}
  .contact.dark{color:var(--ink-dark)}

  /* Letterhead */
  .letterhead{left:99px;top:34px;width:513px;height:656px}
  .letterhead .band{top:0}
  .letterhead .contact{right:12px;top:12px;text-align:right;font-size:8.2px}
  .letterhead .wordmark{left:14px;top:98px;font-size:12.5px}
  .letter{position:absolute;left:140px;top:222px;width:360px;font-family:var(--sans);color:var(--ink)}
  .letter .salutation{font-size:8.5px;font-weight:700;color:#6d6d6d;margin-bottom:36px}
  .letter p{font-size:5.6px;line-height:1.72;margin-bottom:14px;text-align:left}
  .letter .closing{font-size:5.6px;margin-top:22px;color:#777}

  /* Business card */
  .card{left:451px;top:131px;width:211px;height:122px}
  .card .band{top:78px}
  .card .wordmark{left:8px;top:22px;font-size:6.6px;gap:4px}
  .card .wordmark .dot{width:6px;height:6px}
  .card .address{left:8px;top:58px;font-size:5.4px}
  .card .person{position:absolute;right:10px;top:30px;text-align:right;font-family:var(--serif);color:var(--ink-dark)}
  .card .person .name{font-size:8.6px;font-weight:700}
  .card .person .title{font-size:4.6px;font-style:italic;font-weight:700}
  .card .phones{right:10px;top:60px;font-size:4.9px;text-align:right}
  .card .phones span{display:inline-block;width:18px;text-align:left}
  .card .web{position:absolute;right:12px;bottom:5px;font-family:var(--serif);font-weight:700;font-size:5.6px;color:#fff}

  /* Envelope */
  .envelope{left:25px;top:599px;width:568px;height:247px}
  .envelope .band{top:150px}
  .envelope .wordmark{left:12px;top:64px;font-size:12.5px}
  .envelope .web{position:absolute;right:30px;top:25px;font-family:var(--serif);font-weight:700;font-size:9.8px;color:var(--navy-deep)}
  .envelope .contact{left:10px;bottom:12px;font-size:7.6px}
</style>
</head>
<body>
<div class="canvas">
  <div class="stage">

    <section class="sheet letterhead" aria-label="Letterhead">
      <svg class="band" width="513" height="110" viewBox="0 0 513 110" aria-hidden="true">
        <path d="M0 0H513V100C400 72 230 46 0 46Z" fill="var(--navy)"/>
        <path d="M0 46C230 46 400 72 513 100V92C400 64 230 40 0 40Z" fill="var(--navy-soft)"/>
        <path d="M0 52C200 50 380 70 513 104" fill="none" stroke="var(--navy-deep)" stroke-width="3"/>
      </svg>
      <address class="contact light">
        842 East Marlow Avenue, Suite 7B<br>
        Chicago, Illinois 60617<br>
        Tel.&nbsp;&nbsp;312.555.0271<br>
        Fax.&nbsp;&nbsp;312.555.4186<br>
        www.copperglenpartnersllc.example
      </address>
      <div class="wordmark"><span class="dot"></span>Copper Glen Partners LLC</div>

      <div class="letter">
        <div class="salutation">Dear Mr. Hale</div>
        <p>Lorem ipsum dolor sit amet, consectetur adipiscing elit. Vestibulum adipiscing felis ac tortor consectetur feugiat. Etiam malesuada sodales eros ut ornare. Sed lorem eros, mattis id pretium ut, faucibus sit amet quam. Nullam consectetur ultrices ipsum, fringilla porttitor erat ornare ad. Sed sit amet dui vel sapien ultrices vulputate. In hac habitasse platea dictumst. Nam est nisi, rhoncus at sagittis a, porttitor adipiscing nulla. Vivamus placerat felis ultrices quam iaculis eget dignissim felis egestas. Integer nec molestie lorem. Sed odio tellus, vulputate sed laoreet non, vulputate id justo. Etiam suscipit odio vel auctor dictum, felis turpis ullamcorper neque, quis sodales risus metus in magna. Morbi pellentesque justo et quam laoreet facilisis. Aenean placerat, urna ornare aliquet tincidunt, lorem justo molestie ligula, id placerat erat metus nec lectus. Nullam eu ipsum quis turpis tristique iaculis rutrum nec nibh. Phasellus risus eros, semper sit amet faucibus sit amet, laoreet at neque. Donec eros sem, viverra dictum faucibus quis, ullamcorper tincidunt nulla.</p>
        <p>Aenean ut congue tellus. Class aptent taciti sociosqu ad litora torquent per conubia nostra, per inceptos himenaeos. Sed facilisis, velit tincidunt pharetra fermentum, urna tortor iaculis erat, vitae sollicitudin leo mauris quis mi. Cras malesuada sem ac ipsum sagittis ultrices. Mauris fermentum porttitor nisi, eu facilisis lorem consectetur at. Suspendisse est elit, scelerisque ac euismod id, scelerisque viverra odio. Nullam scelerisque metus in eros semper congue. Fusce a fermentum est. Ut ac leo dolor. Quisque dignissim mauris a neque luctus pretium ultrices risus sagittis. Aenean quam massa, rutrum ac hendrerit eu, interdum eu nulla. Curabitur a velit mauris, sed porta eros. Cras id egestas sapien. Proin non metus eget felis eleifend adipiscing. Nunc malesuada pharetra blandit.</p>
        <div class="closing">Your sincerely</div>
      </div>
    </section>

    <section class="sheet card" aria-label="Business card">
      <div class="wordmark"><span class="dot"></span>Copper Glen Partners LLC</div>
      <address class="contact dark address">
        842 East Marlow Avenue, Suite 7B<br>
        Chicago, Illinois 60617
      </address>
      <div class="person">
        <div class="name">Miles T Carver</div>
        <div class="title">Principal</div>
      </div>
      <address class="contact dark phones">
        <span>Tel.</span>312.555.0271<br>
        <span>Fax.</span>312.555.4186<br>
        milestcarver@copperglenpartnersllc.example
      </address>
      <svg class="band" width="211" height="44" viewBox="0 0 211 44" aria-hidden="true">
        <path d="M0 8C70 20 150 24 211 18V44H0Z" fill="var(--navy)"/>
        <path d="M0 4C70 16 150 20 211 14V18C150 24 70 20 0 8Z" fill="var(--navy-soft)"/>
      </svg>
      <div class="web">www.copperglenpartnersllc.example</div>
    </section>

    <section class="sheet envelope" aria-label="Envelope">
      <div class="wordmark"><span class="dot"></span>Copper Glen Partners LLC</div>
      <div class="web">www.copperglenpartnersllc.example</div>
      <svg class="band" width="568" height="97" viewBox="0 0 568 97" aria-hidden="true">
        <path d="M0 22C150 42 380 60 568 58V97H0Z" fill="var(--navy)"/>
        <path d="M0 14C150 34 380 52 568 50V58C380 60 150 42 0 22Z" fill="var(--navy-soft)"/>
        <path d="M0 26C150 46 380 64 568 62" fill="none" stroke="var(--navy-deep)" stroke-width="3"/>
      </svg>
      <address class="contact light">
        842 East Marlow Avenue, Suite 7B<br>
        Chicago, Illinois 60617
      </address>
    </section>

  </div>
</div>
</body>
</html>
```